Business Card Design

We need business cards designed incorporating our graphics/logo already used on our trucks. We are a small construction company that does everything from building new homes, additions, Kitchens, Baths, Decks, Hardwood Floors/Tile, all phases of construction. No job is too small. We pride ourselves on True Craftmanship/Customer Satisfaction, its what truly separates us from everyone else.

Industry/Entity Type

Construction

Contact Information for Business Card

Maple Ridge Renovations Lic#27KT51986400
342 51st Avenue Harbor Point NJ 07912
(555)317-2984 Email: info@mapleridgellc.example
Paul Tremondale

```html
<!DOCTYPE html>
<html lang="en">
<head>
<meta charset="utf-8">
<title>Maple Ridge Renovations – Business Card</title>
<link rel="stylesheet" href="https://fonts.googleapis.com/css2?family=Open+Sans:wght@400;700;800&display=swap">
<style>
  :root {
    --page-bg: #d9d9dc;
    --card-edge: #0d0d0d;
    --tan-light: #e0aa6e;
    --tan-dark: #c98a50;
    --sky-light: #d7eef8;
    --sky: #8fc9e6;
    --banner: #3a3a3a;
    --ink: #1c1c1c;
    --accent-red: #c4262c;
    --service-text: #fbe9d2;
    --logo-text: #1f1f1f;
  }
  * { box-sizing: border-box; margin: 0; padding: 0; }
  html, body { width: 1200px; height: 900px; overflow: hidden; }
  body {
    background: var(--page-bg);
    font-family: "Open Sans", Arial, sans-serif;
    position: relative;
  }
  .card {
    position: absolute;
    left: 110px; top: 170px;
    width: 980px; height: 560px;
    background: var(--card-edge);
    padding: 18px;
    border-radius: 6px;
  }
  .card-face {
    position: relative;
    width: 100%; height: 100%;
    background: linear-gradient(160deg, var(--tan-light), var(--tan-dark));
    overflow: hidden;
  }
  .logo-band {
    position: absolute;
    left: 0; top: 0; width: 100%; height: 180px;
    background: linear-gradient(180deg, var(--sky-light), var(--sky));
    border-bottom: 6px solid var(--card-edge);
  }
  .phone-banner {
    position: absolute;
    left: 330px; top: 14px;
    width: 330px; height: 40px;
    background: var(--banner);
    color: #fff;
    font-weight: 700;
    font-size: 22px;
    letter-spacing: 3px;
    display: flex; align-items: center; justify-content: center;
  }
  .logo-name {
    position: absolute;
    left: 110px; top: 66px;
    width: 620px;
    text-align: center;
    font-weight: 800;
    font-size: 44px;
    line-height: 48px;
    color: var(--logo-text);
    letter-spacing: 2px;
  }
  .logo-art {
    position: absolute;
    right: 40px; top: 30px;
    width: 160px; height: 120px;
  }
  .services {
    position: absolute;
    left: 40px; top: 215px;
    list-style: none;
  }
  .services li {
    color: var(--service-text);
    font-weight: 800;
    font-size: 20px;
    letter-spacing: 1px;
    margin-bottom: 12px;
    display: flex; align-items: center;
  }
  .services li::before {
    content: "";
    width: 10px; height: 10px;
    border-radius: 50%;
    background: var(--ink);
    margin-right: 14px;
  }
  .crew-art {
    position: absolute;
    left: 60px; bottom: 0;
    width: 250px; height: 180px;
  }
  .contact {
    position: absolute;
    left: 440px; top: 215px;
    width: 480px;
    color: var(--ink);
  }
  .contact-name {
    color: var(--accent-red);
    font-weight: 700;
    font-size: 26px;
    margin-bottom: 6px;
  }
  .contact-company {
    font-weight: 700;
    font-size: 20px;
  }
  .contact-address {
    font-size: 19px;
    line-height: 27px;
    margin-bottom: 10px;
  }
  .contact-line {
    display: flex; align-items: center;
    font-size: 20px;
    margin-bottom: 8px;
  }
  .contact-line svg { margin-right: 12px; flex: none; }
</style>
</head>
<body>
  <div class="card">
    <div class="card-face">
      <div class="logo-band"></div>
      <div class="phone-banner">(555) 317-2984</div>
      <div class="logo-name">MAPLE RIDGE RENOVATIONS</div>
      <svg class="logo-art" role="img" aria-label="Illustration of a red biplane over the beach" viewBox="0 0 160 120">
        <rect width="160" height="120" rx="8" fill="#b9605a" opacity="0.55"/>
      </svg>

      <ul class="services">
        <li>REMODELING</li>
        <li>DECKS</li>
        <li>ADDITIONS</li>
      </ul>

      <svg class="crew-art" role="img" aria-label="Cartoon of two builders in hard hats holding lumber" viewBox="0 0 250 180">
        <rect width="250" height="180" rx="10" fill="#5d6f9a" opacity="0.55"/>
      </svg>

      <div class="contact">
        <p class="contact-name">Paul Tremondale</p>
        <p class="contact-company">Maple Ridge Renovations</p>
        <p class="contact-address">Lic#27KT51986400 342 51st Avenue<br>Harbor Point NJ 07912</p>
        <p class="contact-line">
          <svg width="22" height="22" viewBox="0 0 22 22" aria-hidden="true">
            <rect width="22" height="22" rx="3" fill="#c4262c"/>
            <path d="M6 5c1 0 2 2 2 3s-1 1-1 2 3 4 4 4 1-1 2-1 3 1 3 2-1 2-2 2C9 17 5 13 5 7c0-1 0-2 1-2z" fill="#fff"/>
          </svg>
          (555)317-2984
        </p>
        <p class="contact-line">
          <svg width="22" height="22" viewBox="0 0 22 22" aria-hidden="true">
            <rect width="22" height="22" rx="3" fill="#c4262c"/>
            <rect x="4" y="6" width="14" height="10" fill="#fff"/>
            <path d="M4 6l7 6 7-6" fill="none" stroke="#c4262c" stroke-width="1.5"/>
          </svg>
          info@mapleridgellc.example
        </p>
      </div>
    </div>
  </div>
</body>
</html>
```